Community Service Organisation information session flyer

I require a flyer to promote an event. The event is an information session about upcoming community service jobs, where interested people can come along to hear about a new service that is opening in the local area in February 2020.

Target Market(s)

People who currently work in the community service sector (family violence, child wellbeing and aboriginal services)

Industry/Entity Type

Non Profit

Colors

Designer to choose colors to be used in the design.

Requirements
Must have
• The document entitled 'The Maple Gate Community Service Announcement' is the content of the flyer. The 3 most prominent logos need to be 'Wren Lane', 'TLMH' and 'Kelpin and Region Aboriginal Co-Operative' as per the attached. The 'Maple Gate' logo should be 50% smaller, and on the bottom right hand corner.
Nice to have
• Please refer to this website for an idea of the look and feel:
• https://maplegate.example.org/

```html
<!DOCTYPE html>
<html lang="en">
<head>
<meta charset="utf-8">
<title>The Maple Gate – Specialist Practitioners Information Sessions</title>
<link rel="stylesheet" href="https://fonts.googleapis.com/css2?family=Quicksand:wght@400;500;600;700&display=swap">
<style>
  :root {
    --page-bg: #ece8e3;
    --paper: #ffffff;
    --ink: #2b2b2b;
    --ink-soft: #3d3d3d;
    --orange: #f26a0c;
    --orange-light: #f7a35e;
    --peach: #fde3c8;
    --cream: #fff6ec;
    --gold: #f7a823;
    --slate: #55555a;
    --line: #9a9a9a;
  }
  * { box-sizing: border-box; margin: 0; padding: 0; }
  html, body { width: 1200px; height: 1000px; overflow: hidden; }
  body {
    background: var(--page-bg);
    font-family: "Quicksand", sans-serif;
    color: var(--ink);
  }
  .flyer {
    position: absolute;
    left: 247px; top: 0;
    width: 706px; height: 1000px;
    background: var(--paper);
    box-shadow: 0 2px 14px rgba(0,0,0,.12);
    overflow: hidden;
  }
  .hero {
    position: absolute;
    left: 18px; top: 18px;
    width: 670px; height: 277px;
    border-radius: 10px 10px 0 0;
    background: linear-gradient(150deg, var(--cream) 0%, var(--peach) 45%, #f9c08a 100%);
    overflow: hidden;
  }
  .hero-photo {
    position: absolute;
    right: 0; top: 0;
    width: 340px; height: 277px;
    background:
      linear-gradient(90deg, rgba(253,227,200,1) 0%, rgba(253,227,200,0) 35%),
      radial-gradient(ellipse at 60% 35%, #e9d6c4 0%, #cdb9a8 40%, #a8a8a0 75%, #6f7b86 100%);
  }
  .hero-title {
    position: absolute;
    left: 26px; top: 64px;
    font-size: 41px; font-weight: 700;
    letter-spacing: .2px;
    color: var(--ink);
  }
  .hero-subtitle {
    position: absolute;
    left: 26px; top: 118px;
    font-size: 26px; font-weight: 500;
    color: var(--ink-soft);
  }
  .session-band {
    position: absolute;
    left: 0; top: 165px;
    width: 300px; height: 42px;
    background: var(--paper);
    padding-left: 26px;
    font-size: 25px; font-weight: 700;
    line-height: 42px;
    color: #111;
  }
  .intro {
    position: absolute;
    left: 18px; top: 295px;
    width: 670px; height: 260px;
    padding: 18px 26px 0 26px;
    background: linear-gradient(160deg, var(--orange-light) 0%, #f4842e 35%, var(--orange) 70%);
    color: #fff;
    font-size: 12.4px;
    line-height: 16px;
  }
  .intro-lead { font-weight: 700; margin-bottom: 9px; }
  .intro p { margin-bottom: 7px; text-align: justify; }
  .service-list { list-style: none; margin: 4px 0 10px; }
  .service-list li {
    font-weight: 700;
    margin-bottom: 5px;
    display: flex; align-items: center; gap: 6px;
  }
  .tick { width: 10px; height: 10px; flex: none; }
  .event {
    position: absolute;
    left: 18px; top: 555px;
    width: 670px; height: 131px;
    background: var(--slate);
    color: #fff;
    text-align: center;
    padding-top: 16px;
  }
  .event-when { font-size: 21px; font-weight: 700; line-height: 26px; }
  .event-when .date { color: var(--gold); }
  .event-where { font-size: 16px; font-weight: 500; line-height: 20px; }
  .event-note { font-size: 10.8px; line-height: 15px; margin-top: 5px; padding: 0 40px; }
  .about {
    position: absolute;
    left: 44px; top: 697px;
    width: 624px;
    font-size: 12.4px; line-height: 16px;
    color: var(--ink-soft);
  }
  .about p { text-align: justify; margin-bottom: 5px; }
  .partners {
    position: absolute;
    left: 35px; top: 793px;
    width: 635px; height: 92px;
    border: 1px solid var(--line);
    border-radius: 14px;
    display: flex; align-items: center; justify-content: space-around;
    padding: 0 18px;
  }
  .partner {
    display: flex; align-items: center; gap: 8px;
    font-weight: 700; color: var(--ink-soft);
  }
  .partner-mark { width: 12px; height: 12px; border-radius: 50%; background: var(--orange); flex: none; }
  .partner--coop { font-size: 12px; line-height: 14px; width: 170px; }
  .partner--wren { font-size: 26px; color: #2d5f7a; }
  .partner--tlmh { font-size: 32px; font-weight: 500; color: #555; }
  .more-info {
    position: absolute;
    left: 43px; top: 912px;
    font-size: 11.5px; color: var(--ink-soft);
  }
  .web-link {
    display: flex; align-items: center; gap: 8px;
    margin: 5px 0 4px;
    width: 256px; height: 32px;
    border: 1.5px solid #222; border-radius: 5px;
    padding-left: 6px;
    font-size: 13.5px; font-weight: 700; color: #111;
    white-space: nowrap;
  }
  .web-link svg { width: 14px; height: 14px; flex: none; }
  .brand {
    position: absolute;
    right: 44px; top: 940px;
    display: flex; align-items: center; gap: 7px;
    font-size: 15px; font-weight: 700; color: var(--ink-soft);
    white-space: nowrap;
  }
  .brand-mark { width: 12px; height: 12px; border-radius: 50%; background: var(--orange); flex: none; }
  .footer-bar {
    position: absolute;
    left: 0; bottom: 0;
    width: 706px; height: 9px;
    background: var(--orange);
  }
</style>
</head>
<body>
  <main class="flyer">
    <section class="hero">
      <div class="hero-photo" role="img" aria-label="Photograph of a young child blowing on a dandelion outdoors"></div>
      <h1 class="hero-title">The Maple Gate</h1>
      <p class="hero-subtitle">Specialist Practitioners</p>
      <h2 class="session-band">Information Sessions</h2>
    </section>

    <section class="intro">
      <p class="intro-lead">The Maple Gate is part of the State Government’s response to the Independent Inquiry into Family Violence, to strengthen support for children and families and involves a partnership of care agencies</p>
      <p>The services offered by The Maple Gate are:</p>
      <ul class="service-list">
        <li><svg class="tick" viewBox="0 0 10 10"><path d="M1 5.5 L4 8.5 L9 1.5" fill="none" stroke="#3a2a1a" stroke-width="1.8"/></svg>Women, children and young people’s family violence services</li>
        <li><svg class="tick" viewBox="0 0 10 10"><path d="M1 5.5 L4 8.5 L9 1.5" fill="none" stroke="#3a2a1a" stroke-width="1.8"/></svg>Child and family services</li>
        <li><svg class="tick" viewBox="0 0 10 10"><path d="M1 5.5 L4 8.5 L9 1.5" fill="none" stroke="#3a2a1a" stroke-width="1.8"/></svg>Aboriginal services</li>
        <li><svg class="tick" viewBox="0 0 10 10"><path d="M1 5.5 L4 8.5 L9 1.5" fill="none" stroke="#3a2a1a" stroke-width="1.8"/></svg>Men’s family violence services</li>
      </ul>
      <p>Early next year we will be opening in the Northern Ridges area, so we’re currently looking for specialist practitioners who want to be part of this meaningful work.</p>
      <p>If you’re a specialist practitioner in child wellbeing, family violence, Aboriginal services or men’s family violence, we invite you to join us for an information session to learn more about these opportunities.</p>
    </section>

    <section class="event">
      <p class="event-when">Wednesday, <span class="date">October 09, 2019</span> | 3pm and 7pm</p>
      <p class="event-where">the Kelpin &amp; Region Aboriginal Co-Operative office</p>
      <p class="event-where">12 Harbour Lane, Kelpin.</p>
      <p class="event-note">At the information session you’ll have the opportunity to hear from all of the agency partners who are part of The Maple Gate, as well as hear from some current practitioners and ask questions.</p>
    </section>

    <section class="about">
      <p>The Maple Gate is a free service for adults, children and young people who are experiencing, or have experienced, family violence and for families who need extra support with the care of children.</p>
      <p>The aim is to strengthen support for children and families and involves a partnership between Wren Lane, TLMH and the Kelpin &amp; Region Aboriginal Co-Operative.</p>
    </section>

    <section class="partners">
      <div class="partner partner--coop"><span class="partner-mark"></span>Kelpin and Region Aboriginal Co-Operative</div>
      <div class="partner partner--wren">Wren Lane</div>
      <div class="partner partner--tlmh">TLMH</div>
    </section>

    <footer class="more-info">
      <p>For more information, head to</p>
      <p class="web-link"><svg viewBox="0 0 14 14"><circle cx="7" cy="7" r="6" fill="none" stroke="#333" stroke-width="1"/><ellipse cx="7" cy="7" rx="2.6" ry="6" fill="none" stroke="#333" stroke-width="1"/><path d="M1 7h12M2 4h10M2 10h10" stroke="#333" stroke-width="1"/></svg>www.familysafety.example.org</p>
      <p>and check out the latest news section</p>
    </footer>

    <div class="brand"><span class="brand-mark"></span>The Maple Gate</div>
    <div class="footer-bar"></div>
  </main>
</body>
</html>
```